NimbusFern cyber security firm Website

We did our website ourselves on Joomla, it's not great. We want a wordpress based redesign. Some thing that will represent a modern cyber security firm that's aimed at solving business problems.
Https://nimbusfern.co.nz (current site)
#58427c - primary color (you'll know why when you see it's name)
Logo files can be provided. Ask for more info if you need.

We want a modern, quick to load website. Website is going to have a home - services - products - about us - blogs menu. Will need a footer menu, site map, contact page etc.
We getting Content done sperately.
Our logo is #58427c - so hoping for a light theme (or at least the top is).
While we have been specific around the color - we are not after a website that has too much of it.

Reference sites that we like :
https://www.voltaline.co.nz/ - Love the full screen real world image
https://wardvex.co.nz/ (love the real world imagry and motion)
https://www.qtr.com/us-en?lnk=m
https://redowlen.com

Please dont use :
cartoon or redered images : (Like this : https://img.stockmorra.com/free-vector/cyber-security-concept_23-2148543851.jpg?w=2000 )

Please don't use images like this : https://www.tavelundi.com/eu/blog/oil-gas/app/uploads/2020/04/116137226_s-1440x564_c.jpg - they are old and boring.

We would like to see some creativity - loading our logo into a readymade wordpress template and hitting go won't cut it.
Updates

Thanks everyone who has submitted so far. We've extended the deadline as we wanted to give everyone a chance to Re- read the brief and perhaps make some tweeks should they feel it necessary.

Target Market(s)

Mid - large enterprise, finance, insurance, utilities vertical

Industry/Entity Type

Cyber security

Coding

Coded - Design and coding required

Number of Pages Required

5+ page

Font styles to use
Other font styles liked:
• Open sans

Colors

Designer to choose colors to be used in the design.

Requirements
Must have
• Simple clear messaging, something that catches user engagement
Nice to have
• Motion of some sort, but not overdone, GDPR

```html
<!DOCTYPE html>
<html lang="en">
<head>
<meta charset="utf-8">
<title>NimbusFern — Third-Party Risk Management</title>
<link rel="stylesheet" href="https://fonts.googleapis.com/css2?family=Lexend:wght@300;400;500;600;700&family=Open+Sans:wght@300;400;600;700&display=swap">
<style>
:root{
  --primary:#58427c;
  --primary-dark:#45305f;
  --ink:#3f3358;
  --text:#4d4760;
  --muted:#6f6a7d;
  --lavender:#e9e4f1;
  --lavender-mid:#c9bedb;
  --lavender-soft:#f3f0f7;
  --white:#ffffff;
  --green:#3aa14a;
}
*{margin:0;padding:0;box-sizing:border-box}
html,body{width:1200px;height:3416px;overflow:hidden;background:var(--white)}
body{position:relative;font-family:"Open Sans",sans-serif;color:var(--text)}
.abs{position:absolute}
.heading{font-family:"Lexend",sans-serif}

/* header */
.brand{display:flex;align-items:center;gap:10px;font-family:"Lexend",sans-serif;font-weight:500;color:var(--primary);letter-spacing:1px}
.brand-dot{width:30px;height:30px;border-radius:50%;background:var(--primary)}
.site-brand{left:60px;top:26px;font-size:28px}
.main-nav{left:627px;top:31px;display:flex;gap:27px;font-family:"Lexend",sans-serif;font-size:13px;color:var(--ink)}
.main-nav a{position:relative;color:inherit;text-decoration:none}
.main-nav a.active{color:var(--primary)}
.main-nav a.active::after{content:"";position:absolute;left:50%;top:22px;margin-left:-4px;border:4px solid transparent;border-bottom:6px solid var(--primary)}
.pill-btn{display:flex;align-items:center;gap:12px;background:var(--primary);color:var(--white);border-radius:30px;font-family:"Lexend",sans-serif;font-weight:500;letter-spacing:.5px}
.pill-icon{background:var(--white);border-radius:50%;border:3px solid var(--primary);box-shadow:0 0 0 2px var(--white)}
.contact-btn{left:972px;top:20px;width:167px;height:40px;padding:0 4px;font-size:14px}
.contact-btn .pill-icon{width:34px;height:34px}

/* hero */
.hero-title{left:57px;top:200px;font-family:"Lexend",sans-serif;font-weight:700;font-size:59px;line-height:60px;color:var(--primary);letter-spacing:-.5px}
.hero-sub{left:62px;top:342px;font-size:15px;line-height:22px;color:var(--ink);width:400px}
.demo-btn{left:60px;top:413px;width:202px;height:39px;padding:0 3px;font-size:14px}
.demo-btn .pill-icon{width:32px;height:32px}
.learn-link{left:283px;top:423px;font-family:"Lexend",sans-serif;font-size:14px;color:var(--primary);text-decoration:underline}
.dashboard{left:667px;top:170px;width:453px;height:268px;border-radius:14px;background:linear-gradient(180deg,#dcd8e2,#f7f7f9 8%,#ffffff 60%,#e7e4ec);border:8px solid #d9d6df}
.stat-card{left:528px;top:365px;width:337px;height:126px;background:var(--white);border:1.5px solid var(--primary);border-radius:16px;box-shadow:0 6px 18px rgba(88,66,124,.15)}
.stat{position:absolute;top:22px;text-align:center;font-size:11px;color:var(--ink)}
.stat b{display:block;font-family:"Lexend",sans-serif;font-weight:600;font-size:18px;color:var(--primary)}
.stat-bar{position:absolute;left:18px;right:18px;top:78px;height:7px;border-radius:4px;background:linear-gradient(90deg,#2f9a3e,#b7c22b 45%,#e08a23 75%,#9a1b2c)}
.stat-mark{position:absolute;left:72px;top:72px;width:4px;height:18px;background:var(--primary)}
.stat-note{position:absolute;left:0;right:0;top:96px;text-align:center;font-size:11px;color:var(--ink)}
.slider{left:60px;top:538px;display:flex;align-items:center;gap:12px}
.slider i{display:block;width:58px;height:1.5px;background:var(--primary)}

/* intro */
.intro{left:0;width:1200px;text-align:center}
.intro-title{top:778px;font-family:"Lexend",sans-serif;font-weight:600;font-size:36px;color:var(--primary);letter-spacing:.5px}
.intro-title-light{top:820px;font-family:"Lexend",sans-serif;font-weight:300;font-size:33px;color:var(--primary);letter-spacing:.5px}
.intro-lead{top:884px;font-size:14px;line-height:23px;color:var(--ink)}
.intro-sub{top:960px;font-family:"Lexend",sans-serif;font-weight:500;font-size:18px;line-height:25px;color:var(--primary)}
.intro-body{font-size:12.5px;line-height:22.5px;color:var(--muted);font-weight:300}

/* benefit panel */
.benefits{left:60px;top:1367px;width:1080px;height:359px;border-radius:70px;background:linear-gradient(120deg,#3f2c5e,#58427c 55%,#4b356c);overflow:hidden}
.benefit-photo{position:absolute;left:126px;top:45px;width:324px;height:314px;background:linear-gradient(180deg,#6c5890,#2f2540);border-radius:140px 140px 0 0}
.benefit-list{position:absolute;left:518px;top:71px;list-style:none;color:var(--white);font-size:15.5px}
.benefit-list li{display:flex;align-items:center;gap:14px;height:46px}

/* partners */
.partner{position:absolute;top:1790px;width:260px;margin-left:-130px;text-align:center;font-family:"Open Sans",sans-serif;font-weight:700;font-size:15.5px;line-height:23px;color:var(--primary)}
.partner-mark{height:74px;display:flex;align-items:center;justify-content:center;gap:10px;margin-bottom:38px;font-family:"Open Sans",sans-serif;font-weight:600;font-size:26px;color:#6a6a6a}
.partner-badge{width:74px;height:74px;border-radius:50%;background:#2f2f2f}
.partner-square{width:38px;height:38px;background:#7a7a7a}

/* services */
.services-title{left:0;width:1200px;top:2092px;text-align:center;font-family:"Lexend",sans-serif;font-weight:600;font-size:35px;color:var(--primary);letter-spacing:1px}
.tab{position:absolute;left:60px;width:338px;height:51px;border-radius:14px;background:var(--lavender);display:flex;align-items:center;padding-left:25px;font-size:15px;color:var(--primary)}
.tab.active{background:var(--white);border:1.5px solid var(--primary);font-family:"Lexend",sans-serif;font-size:18px}
.tab-rule{left:425px;top:2208px;width:1px;height:457px;background:var(--lavender-mid)}
.tab-dot{left:421px;top:2224px;width:9px;height:9px;border-radius:50%;background:var(--primary)}
.service-heading{left:497px;top:2200px;font-family:"Lexend",sans-serif;font-size:41px;font-weight:500;color:transparent;-webkit-text-stroke:1.2px var(--primary)}
.service-heading b{color:var(--primary);-webkit-text-stroke:0;font-weight:700}
.service-photo{left:497px;top:2254px;width:325px;height:240px;border-radius:6px;background:linear-gradient(180deg,#c9c6d2,#8e8aa0 60%,#5e5a70)}
.service-text{left:504px;top:2512px;width:548px;font-size:13.3px;line-height:21px;color:var(--muted)}
.service-btn{left:506px;top:2626px;width:170px;height:39px;padding:0 3px;font-size:14px}
.service-btn .pill-icon{width:32px;height:32px}

.gdpr{left:0;top:2745px;width:1200px;height:66px;background:var(--primary);color:var(--white);display:flex;align-items:center;justify-content:center;gap:18px;font-family:"Lexend",sans-serif;font-size:27px;letter-spacing:1px}

/* social */
.social{position:absolute;top:2893px;width:140px;margin-left:-70px;text-align:center;font-family:"Lexend",sans-serif;font-size:19px;color:var(--primary)}
.social-mark{width:48px;height:48px;margin:0 auto 15px;border-radius:50%;background:var(--white);border:3px solid var(--primary);box-shadow:inset 0 0 0 6px var(--white),inset 0 0 0 30px var(--lavender-mid)}

/* footer */
.footer-brand{left:60px;top:3212px;font-size:28px}
.footer-social{left:100px;top:3258px;display:flex;gap:5px}
.footer-social i{display:block;width:38px;height:38px;border-radius:50%;background:var(--primary)}
.f-col{position:absolute;top:3154px}
.f-col h4{font-family:"Lexend",sans-serif;font-weight:500;font-size:15px;color:var(--primary);margin-bottom:12px}
.f-col ul{list-style:none;font-size:12px;color:var(--muted)}
.f-col li{height:22.5px;display:flex;align-items:center;gap:15px}
.f-col li::before{content:"";width:6px;height:6px;border:1px solid var(--primary);border-radius:50%}
.f-col.contact li{height:auto;align-items:flex-start;margin-bottom:12px;line-height:19px}
.f-col.contact li::before{display:none}
.footer-rule{left:60px;top:3364px;width:1080px;height:1px;background:var(--lavender-mid)}
.copyright{left:62px;top:3383px;font-size:11.5px;color:var(--ink)}
.copyright b{color:var(--primary)}
.legal{right:62px;top:3383px;font-size:11.5px;color:var(--ink);word-spacing:3px}
</style>
</head>
<body>

<!-- hero background -->
<svg class="abs" style="left:0;top:0" width="1200" height="730" viewBox="0 0 1200 730" aria-hidden="true">
  <defs>
    <linearGradient id="heroGlow" x1="0" y1="0" x2="1" y2="0.3">
      <stop offset="0" stop-color="#ffffff"/>
      <stop offset="0.45" stop-color="#f1eef6"/>
      <stop offset="1" stop-color="#b5a7cc"/>
    </linearGradient>
    <linearGradient id="heroWave" x1="0" y1="0" x2="1" y2="0">
      <stop offset="0" stop-color="#c3b8d6"/>
      <stop offset="1" stop-color="#6d5a92"/>
    </linearGradient>
  </defs>
  <rect width="1200" height="730" fill="url(#heroGlow)"/>
  <path d="M0 520 C180 620 330 640 520 600 C700 560 840 470 1000 470 C1100 470 1160 500 1200 520 L1200 730 L0 730Z" fill="url(#heroWave)"/>
  <path d="M0 560 C200 700 380 690 600 650 C800 610 980 540 1200 540 L1200 730 L0 730Z" fill="#ffffff" opacity=".55"/>
  <path d="M0 640 C220 720 420 700 620 680 C820 660 1000 620 1200 600 L1200 730 L0 730Z" fill="#ffffff"/>
</svg>

<header>
  <div class="abs brand site-brand"><span class="brand-dot"></span>NIMBUSFERN</div>
  <nav class="abs main-nav">
    <a class="active" href="#">Home</a><a href="#">Services</a><a href="#">Products</a><a href="#">About Us</a><a href="#">Blog</a>
  </nav>
  <a class="abs pill-btn contact-btn" href="#"><span class="pill-icon"></span>CONTACT US</a>
</header>

<section class="hero">
  <h1 class="abs hero-title">Third-Party Risk<br>Management</h1>
  <p class="abs hero-sub">All your Third-party vendor and supply chain risks detailed in a single place.</p>
  <a class="abs pill-btn demo-btn" href="#"><span class="pill-icon"></span>DEMO PLATFORM</a>
  <a class="abs learn-link" href="#">LEARN MORE</a>
  <div class="abs dashboard" role="img" aria-label="Laptop showing the vendor risk dashboard table"></div>
  <div class="abs stat-card">
    <div class="stat" style="left:28px">
      <b>384K</b>minimum</div>
    <div class="stat" style="left:134px">
      <b style="font-size:23px">31.1M</b>Most likely</div>
    <div class="stat" style="left:258px">
      <b>985</b>Maximum</div>
    <div class="stat-bar"></div>
    <div class="stat-mark"></div>
    <div class="stat-note">The Probable annualized loss for an organization.</div>
  </div>
  <div class="abs slider">
    <i></i>
    <svg width="30" height="20" viewBox="0 0 30 20" aria-hidden="true"><path d="M10 2 L3 10 L10 18 M20 2 L27 10 L20 18" fill="none" stroke="#58427c" stroke-width="1.6"/></svg>
  </div>
</section>

<section class="intro-section">
  <h2 class="abs intro intro-title">THIRD-PARTY RISK</h2>
  <p class="abs intro intro-title-light">MANAGEMENT</p>
  <p class="abs intro intro-lead">We Provide The Full Detail, Providing A Multidimensional View Of Your Entire Attack Surface<br>From A &nbsp;Technical, Financial Impact And A Compliance Perspective.</p>
  <h3 class="abs intro intro-sub">The Tech You Use To Run Your Business Could Be Used<br>To Sabotage It!</h3>
  <p class="abs intro intro-body" style="top:1033px">In the course of doing business, your company could deal with dozens of third-party vendors: suppliers,<br>manufacturers, service providers, affiliate offices, distributors, resellers, agents, contractors, the list goes<br>on … all of whom, in turn, deal with dozens of their own vendors. &nbsp;It’s easy to see then why third-party<br>cyber risk management is becoming such a high priority for businesses that deal with confidential data.<br>(Lawyers, accountants, insurers, to name just three.)</p>
  <p class="abs intro intro-body" style="top:1160px">NimbusFern is a 100% New Zealand owned and operated cyber security company, designed to protect<br>your business against exactly this kind of risk by offering third-party risk management and cyber<br>security solutions.</p>
  <p class="abs intro intro-body" style="top:1241px">In short, offering small and medium sized businesses the same standard of cyber security as a large<br>organisations – at a price that makes sense.</p>
</section>

<section class="abs benefits">
  <div class="benefit-photo" role="img" aria-label="Photo of a businessman in a suit using a tablet"></div>
  <ul class="benefit-list">
    <li><svg width="14" height="14" viewBox="0 0 14 14" aria-hidden="true"><circle cx="7" cy="7" r="6" fill="none" stroke="#fff" stroke-width="1.4"/><path d="M4 7 L6.3 9.3 L11 4.5" fill="none" stroke="#fff" stroke-width="1.4"/></svg>Reduce your Third-party risk management from weeks to hours</li>
    <li><svg width="14" height="14" viewBox="0 0 14 14" aria-hidden="true"><circle cx="7" cy="7" r="6" fill="none" stroke="#fff" stroke-width="1.4"/><path d="M4 7 L6.3 9.3 L11 4.5" fill="none" stroke="#fff" stroke-width="1.4"/></svg>Get the full vendor risk view across your whole supply chain</li>
    <li><svg width="14" height="14" viewBox="0 0 14 14" aria-hidden="true"><circle cx="7" cy="7" r="6" fill="none" stroke="#fff" stroke-width="1.4"/><path d="M4 7 L6.3 9.3 L11 4.5" fill="none" stroke="#fff" stroke-width="1.4"/></svg>Calculate, continuously monitor and reduce your cyber security risk.</li>
    <li><svg width="14" height="14" viewBox="0 0 14 14" aria-hidden="true"><circle cx="7" cy="7" r="6" fill="none" stroke="#fff" stroke-width="1.4"/><path d="M4 7 L6.3 9.3 L11 4.5" fill="none" stroke="#fff" stroke-width="1.4"/></svg>Save time and resources in cyber risk assessments</li>
    <li><svg width="14" height="14" viewBox="0 0 14 14" aria-hidden="true"><circle cx="7" cy="7" r="6" fill="none" stroke="#fff" stroke-width="1.4"/><path d="M4 7 L6.3 9.3 L11 4.5" fill="none" stroke="#fff" stroke-width="1.4"/></svg>Extremely competitive pricing.</li>
  </ul>
</section>

<section class="partners">
  <div class="partner" style="left:208px"><div class="partner-mark"><span class="partner-badge"></span></div>100% NZ owned &amp;<br>Operated</div>
  <div class="partner" style="left:472px"><div class="partner-mark"><span class="partner-square"></span>Solvane</div>New Zealand<br>Datacentre Cloud Only</div>
  <div class="partner" style="left:749px"><div class="partner-mark" style="font-size:20px;color:#222">Red Owlen</div>Red Owlen Partners Only<br>NZ Red Owlen Partner</div>
  <div class="partner" style="left:988px"><div class="partner-mark" style="color:#1ba0d7">Corvix</div>Corvix Partner</div>
</section>

<!-- services background -->
<svg class="abs" style="left:0;top:1985px" width="1200" height="765" viewBox="0 0 1200 765" aria-hidden="true">
  <defs>
    <linearGradient id="servicesFill" x1="0" y1="0" x2="0" y2="1">
      <stop offset="0" stop-color="#e6e0ef"/>
      <stop offset="0.6" stop-color="#f4f1f8"/>
      <stop offset="1" stop-color="#c6bad9"/>
    </linearGradient>
  </defs>
  <path d="M0 40 C80 20 120 30 160 40 C260 10 420 0 600 0 C780 0 960 30 1050 60 C1120 40 1170 30 1200 40 L1200 765 L0 765Z" fill="#efedf3"/>
  <path d="M0 200 C150 80 380 50 600 50 C820 50 1050 90 1200 200 L1200 765 L0 765Z" fill="url(#servicesFill)"/>
</svg>

<section class="services">
  <h2 class="abs services-title">SERVICES</h2>
  <div class="tab active" style="top:2205px">Virtual Corvix CISO</div>
  <div class="tab" style="top:2267px">Cyber Security Assessments</div>
  <div class="tab" style="top:2330px">Third-Party Risk Management</div>
  <div class="tab" style="top:2392px">Human Risk Management</div>
  <div class="tab" style="top:2455px">Cyber Security Warrant of Fitness</div>
  <div class="abs tab-rule"></div>
  <div class="abs tab-dot"></div>
  <h3 class="abs service-heading">Virtual Corvix <b>CISO</b></h3>
  <div class="abs service-photo" role="img" aria-label="Photo of a smiling consultant pointing at a laptop showing the vCISO service wheel"></div>
  <p class="abs service-text">The vCISO is a security practitioner who uses the culmination of their years of cybersecurity and industry experience to help organizations with developing and managing the implementation of the organization’s information security program. At a high level, vCISOs help to architect the organization’s security strategy, with some helping to also manage its’ implementation.</p>
  <a class="abs pill-btn service-btn" href="#"><span class="pill-icon"></span>LEARN MORE</a>
</section>

<a class="abs gdpr" href="#" style="text-decoration:none">GDPR
  <svg width="40" height="14" viewBox="0 0 40 14" aria-hidden="true"><path d="M0 7 H38 M31 1 L38 7 L31 13" fill="none" stroke="#fff" stroke-width="1.5"/></svg>
</a>

<section class="socials">
  <div class="social" style="left:354px"><div class="social-mark"></div>Linkora</div>
  <div class="social" style="left:520px"><div class="social-mark"></div>Meetbook</div>
  <div class="social" style="left:686px"><div class="social-mark"></div>Chirply</div>
  <div class="social" style="left:846px"><div class="social-mark"></div>Streamly</div>
</section>

<!-- footer background -->
<svg class="abs" style="left:0;top:3030px" width="1200" height="386" viewBox="0 0 1200 386" aria-hidden="true">
  <path d="M0 20 C120 60 220 80 340 60 C520 30 640 10 820 30 C960 45 1080 20 1200 0 L1200 386 L0 386Z" fill="#d6cee3"/>
  <path d="M0 50 C140 90 260 110 400 90 C560 70 700 50 860 65 C1000 78 1100 60 1200 40 L1200 386 L0 386Z" fill="#f4f2f7"/>
</svg>

<footer>
  <div class="abs brand footer-brand"><span class="brand-dot"></span>NIMBUSFERN</div>
  <div class="abs footer-social"><i></i><i></i><i></i><i></i></div>
  <div class="f-col" style="left:387px">
    <h4>SITEMAP</h4>
    <ul><li>Home</li><li>Services</li><li>Products</li><li>About us</li><li>Blogs</li></ul>
  </div>
  <div class="f-col" style="left:595px">
    <h4>SERVICES</h4>
    <ul><li>Virtual Corvix CISO</li><li>Information Security Officer</li><li>Cyber Threat Security assessments</li><li>Third-party Risk Management</li><li>Human Risk Management</li><li>Cyber Security Warrant of Fitness</li></ul>
  </div>
  <div class="f-col contact" style="left:887px">
    <h4>CONTACTUS</h4>
    <ul>
      <li><svg width="22" height="22" viewBox="0 0 22 22" aria-hidden="true"><path d="M5 2 L9 6 L7 9 C8 12 10 14 13 15 L16 13 L20 17 L17 20 C9 19 3 13 2 5Z" fill="none" stroke="#58427c" stroke-width="1.3"/></svg><span style="margin-left:14px">+64 (0) 210 555 0142</span></li>
      <li><svg width="22" height="22" viewBox="0 0 22 22" aria-hidden="true"><rect x="2" y="5" width="18" height="13" fill="none" stroke="#58427c" stroke-width="1.3"/><path d="M2 5 L11 12 L20 5" fill="none" stroke="#58427c" stroke-width="1.3"/></svg><span style="margin-left:14px">info@nimbusfern.co.nz</span></li>
      <li><svg width="22" height="26" viewBox="0 0 22 26" aria-hidden="true"><path d="M11 24 C5 16 3 12 3 9 A8 8 0 0 1 19 9 C19 12 17 16 11 24Z" fill="none" stroke="#58427c" stroke-width="1.3"/><circle cx="11" cy="9" r="3" fill="none" stroke="#58427c" stroke-width="1.3"/></svg><span style="margin-left:14px">48b Koru Lane, Tarawa,<br>Westhaven, 4391</span></li>
    </ul>
  </div>
  <div class="abs footer-rule"></div>
  <p class="abs copyright">©<b>NIMBUSFERN</b> -2022 All rights reserved.</p>
  <p class="abs legal">Terms &amp; Conditions | Privacy | Cookies Policy | GDPR</p>
</footer>

</body>
</html>
```